Beekeeper needs box/label design for honey/CBD and other honey-related products

We need a box (or label) design for a beekeeping company in Virginia called Larkmoor Hollow Farm. Our products will include honey mixed with CBD oil and other essential oils (vanilla, lavender, etc).The box design should be scalable to include several different honey/oil products. We would like to incorporate our current farm logo into the design. Here is a link to a honey producing company with a series of products using their honey mixed with certain oils. It's a good reference of what type box/label design we would like (https://pipandwrenly.co/pages/honey).

Target Market(s)

Retail stores and consumers

Requirements
Must have
• Larkmoor Hollow Farm name and logo

```html
<!DOCTYPE html>
<html lang="en">
<head>
<meta charset="utf-8">
<title>Larkmoor Hollow Farm – Raw Honey Infused with CBD, Lavender Essence</title>
<link rel="stylesheet" href="https://fonts.googleapis.com/css2?family=Roboto+Slab:wght@300;400;800&family=Roboto+Condensed:wght@700&display=swap">
<style>
  :root {
    --page-bg: #eeeeee;
    --essence-main: #8a97c3;
    --essence-deep: #5a3c9c;
    --essence-motif: #6f74b6;
    --tab-white: #ffffff;
    --brand-green: #5f6b22;
    --text-light: #ffffff;
    --text-soft: #eef0f8;
    --note-ink: #111111;
  }
  * { box-sizing: border-box; margin: 0; padding: 0; }
  html, body { width: 1200px; height: 1061px; overflow: hidden; }
  body {
    background: var(--page-bg);
    font-family: "Roboto Slab", Georgia, serif;
    position: relative;
  }
  .panel {
    position: absolute;
    background: var(--essence-main);
    overflow: hidden;
    color: var(--text-light);
    text-align: center;
  }
  .panel--label { left: 177px; top: 393px; width: 366px; height: 380px; }
  .panel--box { left: 618px; top: 193px; width: 418px; height: 673px; }

  .motif-strip {
    position: absolute;
    top: 0; right: 0; bottom: 0;
    background: linear-gradient(90deg, rgba(111,116,182,0) 0%, var(--essence-motif) 100%);
  }
  .panel--label .motif-strip { width: 120px; }
  .panel--box .motif-strip { width: 130px; }

  .brand-tab {
    position: absolute;
    top: 0;
    background: var(--tab-white);
    clip-path: polygon(0 0, 100% 0, 100% 88%, 50% 100%, 0 88%);
    display: flex;
    flex-direction: column;
    align-items: center;
    padding-top: 20px;
    gap: 12px;
  }
  .panel--label .brand-tab { left: 38px; width: 117px; height: 145px; }
  .panel--box .brand-tab { left: 46px; width: 144px; height: 155px; padding-top: 22px; }
  .brand-tab__mark {
    width: 58px; height: 58px;
    background: var(--brand-green);
  }
  .panel--box .brand-tab__mark { width: 70px; height: 70px; }
  .brand-tab__name {
    font-weight: 400;
    color: var(--brand-green);
    font-size: 14px;
    line-height: 1.15;
    width: 100%;
    padding: 0 6px;
  }
  .panel--box .brand-tab__name { font-size: 16px; }

  .product-title {
    position: absolute;
    left: 0; right: 0;
    font-weight: 800;
    letter-spacing: 1px;
    line-height: 1;
    color: var(--text-soft);
  }
  .product-subtitle {
    position: absolute;
    left: 0; right: 0;
    font-weight: 300;
    line-height: 1;
    color: var(--text-soft);
  }
  .product-subtitle strong { font-weight: 800; }
  .panel--label .product-title { top: 160px; font-size: 44px; }
  .panel--label .product-subtitle { top: 212px; font-size: 29px; }
  .panel--box .product-title { top: 294px; font-size: 46px; }
  .panel--box .product-subtitle { top: 350px; font-size: 30px; }

  .essence-band {
    position: absolute;
    background: var(--essence-deep);
    color: var(--text-light);
    font-weight: 800;
    letter-spacing: 1px;
    display: flex;
    align-items: center;
    justify-content: center;
  }
  .panel--label .essence-band { left: 30px; width: 282px; top: 255px; height: 38px; font-size: 20px; }
  .panel--box .essence-band { left: 0; right: 0; top: 392px; height: 42px; font-size: 21px; }

  .net-weight {
    position: absolute;
    left: 0; right: 0;
    font-weight: 400;
    color: var(--text-soft);
  }
  .panel--label .net-weight { top: 313px; font-size: 18px; padding-right: 20px; }
  .panel--box .net-weight { top: 582px; font-size: 20px; }

  .color-note__lines { position: absolute; left: 0; top: 0; }
  .color-note {
    position: absolute;
    left: 417px; top: 940px;
    font-family: "Roboto Condensed", Arial, sans-serif;
    font-weight: 700;
    font-size: 20px;
    line-height: 1.4;
    color: var(--note-ink);
  }
</style>
</head>
<body>
  <section class="panel panel--label" aria-label="Jar label">
    <div class="motif-strip" role="img" aria-label="Pattern of hemp leaves and honey bees in deep violet"></div>
    <div class="brand-tab">
      <span class="brand-tab__mark"></span>
      <span class="brand-tab__name">Larkmoor Hollow Farm</span>
    </div>
    <h1 class="product-title">RAW HONEY</h1>
    <p class="product-subtitle">INFUSED WITH <strong>CBD</strong></p>
    <p class="essence-band">LAVENDER ESSENCE</p>
    <p class="net-weight">16 ounces (454 grams)</p>
  </section>

  <section class="panel panel--box" aria-label="Box front">
    <div class="motif-strip" role="img" aria-label="Pattern of hemp leaves and honey bees in deep violet"></div>
    <div class="brand-tab">
      <span class="brand-tab__mark"></span>
      <span class="brand-tab__name">Larkmoor Hollow Farm</span>
    </div>
    <h2 class="product-title">RAW HONEY</h2>
    <p class="product-subtitle">INFUSED WITH <strong>CBD</strong></p>
    <p class="essence-band">LAVENDER ESSENCE</p>
    <p class="net-weight">16 ounces (454 grams)</p>
  </section>

  <svg class="color-note__lines" width="1200" height="1061" aria-hidden="true">
    <polyline points="447,760 558,922 658,806" fill="none" stroke="#111" stroke-width="1"/>
  </svg>
  <p class="color-note">MAIN COLOR WILL CHANGE<br>ACCORDING THE ESSENCE</p>
</body>
</html>
```